A4 Client Referral Program Flyer for Property Management Agency

Harbourleaf Estates Agency is a property management specialist based on Sydney's Northern Beaches in Australia.

We manage mid to high-end rental properties for investors and property owners.
We are currently looking to build our portfolio and are offering existing clients and contacts a referral incentive. We want to sign up more properties to manage.

We are offering the referrer a $250 referral fee and the new owner 2 months of free management to entice them to use Harbourleaf Estates Agency.

We want an A4 Flyer to print and add to other document packages we hand out to clients and suppliers.
If at all possible a matching digital banner would be great too! 1000px wide x 250px

Please find copy attached in Word Doc and our logo attached also.

Please see our website for any more details on our business.

We must be able to have an editable photoshop version (PSD) of the document as well as a print ready PDF version incl any bleed necessary for A4 printing.

Target Market(s)

30-60YO Male and Female

Industry/Entity Type

Real Estate

Font styles to use
Sans Serif

Requirements
Must have
• Company Logo, contact details and copy provided

```html
<!DOCTYPE html>
<html lang="en">
<head>
<meta charset="utf-8">
<title>Harbourleaf Estates Agency – Referral Flyer and Banner</title>
<link href="https://fonts.googleapis.com/css2?family=Hind:wght@300;400;600;700&display=swap" rel="stylesheet">
<style>
  :root {
    --navy: #243559;
    --navy-deep: #142a4c;
    --teal: #1d8596;
    --teal-box: rgba(29, 133, 150, 0.92);
    --facade: #7c8794;
    --grey-band: #e3e3e3;
    --ink: #1a1a1a;
    --muted: #3c3c3c;
    --white: #ffffff;
    --backdrop: #eceae6;
  }
  * { box-sizing: border-box; margin: 0; padding: 0; }
  html, body { width: 1200px; height: 1200px; overflow: hidden; }
  body { background: var(--backdrop); font-family: "Hind", Arial, sans-serif; position: relative; }

  /* ---------- A4 flyer ---------- */
  .flyer {
    position: absolute; left: 90px; top: 28px; width: 640px; height: 905px;
    background: var(--navy); overflow: hidden;
    box-shadow: 0 6px 18px rgba(0,0,0,0.18);
  }
  .flyer__header { position: absolute; left: 0; top: 0; width: 640px; height: 200px; background: var(--navy); }
  .flyer__rule { position: absolute; top: 90px; height: 20px; background: var(--teal); }
  .flyer__rule--left { left: 0; width: 115px; }
  .flyer__rule--right { right: 0; width: 123px; }
  .flyer__brand {
    position: absolute; left: 135px; top: 72px; width: 370px; text-align: center;
    color: var(--white); font-weight: 600; font-size: 27px; line-height: 1.05; letter-spacing: 0.5px; text-transform: uppercase;
  }
  .flyer__photo {
    position: absolute; left: 0; top: 170px; width: 640px; height: 523px;
    background: linear-gradient(180deg, var(--navy) 0%, #3d4a66 22%, var(--facade) 60%, #5d6878 100%);
  }
  .offer {
    position: absolute; left: 231px; top: 269px; width: 409px; height: 256px;
    background: var(--teal-box); color: var(--white); padding: 40px 0 0 45px;
  }
  .offer__lead { font-weight: 600; font-size: 28px; line-height: 1.15; letter-spacing: 0.4px; text-transform: uppercase; }
  .offer__amount { font-weight: 700; font-size: 60px; line-height: 1; margin-top: 6px; letter-spacing: -1px; }
  .offer__sub { font-weight: 300; font-size: 26px; line-height: 1.1; margin-top: 8px; }
  .offer__perk { font-weight: 700; font-size: 26px; line-height: 1.2; text-transform: uppercase; }

  .terms {
    position: absolute; left: 0; top: 693px; width: 640px; height: 80px; background: var(--grey-band);
    color: var(--muted); font-size: 10.6px; line-height: 1.35; text-align: center; padding: 22px 30px 0;
  }
  .flyer__footer { position: absolute; left: 0; top: 773px; width: 640px; height: 120px; background: var(--white); }
  .flyer__footer-brand {
    position: absolute; left: 40px; top: 44px; width: 220px; color: var(--ink);
    font-weight: 600; font-size: 18px; line-height: 1.1; text-transform: uppercase;
  }
  .contact-list { position: absolute; left: 304px; top: 38px; list-style: none; }
  .contact-list li { display: flex; align-items: center; gap: 10px; height: 23.5px; font-size: 14.5px; color: var(--muted); font-weight: 400; }
  .contact-icon { width: 15px; height: 15px; flex: none; }
  .flyer__base { position: absolute; left: 0; bottom: 0; width: 640px; height: 12px; background: var(--teal); }

  /* ---------- 1000 x 250 banner (shown at 80%) ---------- */
  .banner {
    position: absolute; left: 370px; top: 970px; width: 800px; height: 200px; overflow: hidden;
    box-shadow: 0 6px 18px rgba(0,0,0,0.18);
  }
  .banner__photo {
    position: absolute; inset: 0;
    background: linear-gradient(90deg, var(--navy-deep) 0%, var(--navy-deep) 35%, #354664 55%, #6d7888 80%, #4d5868 100%);
  }
  .banner__brand {
    position: absolute; left: 18px; top: 70px; width: 300px; color: var(--white);
    font-weight: 600; font-size: 26px; line-height: 1.05; text-transform: uppercase;
  }
  .banner__contacts { position: absolute; right: 512px; top: 148px; list-style: none; text-align: right; }
  .banner__contacts li { display: flex; justify-content: flex-end; align-items: center; gap: 8px; height: 15px; color: var(--white); font-size: 11.5px; font-weight: 300; }
  .banner__contacts .contact-icon { width: 10px; height: 10px; }
  .banner__offer {
    position: absolute; left: 444px; top: 28px; width: 308px; height: 148px; background: var(--teal-box);
    color: var(--white); text-align: center; padding-top: 10px;
  }
  .banner__offer .offer__lead { font-size: 19px; line-height: 1.1; }
  .banner__offer .offer__amount { font-size: 40px; margin-top: 2px; }
  .banner__offer .offer__sub { font-size: 17px; margin-top: 2px; }
  .banner__offer .offer__perk { font-size: 17px; }
</style>
</head>
<body>

<svg width="0" height="0" style="position:absolute">
  <defs>
    <symbol id="icon-web" viewBox="0 0 16 16"><circle cx="8" cy="8" r="8" fill="#1d8596"/><circle cx="8" cy="8" r="3" fill="none" stroke="#fff" stroke-width="1.3"/><path d="M11 8v1.3a1.4 1.4 0 0 0 2.6 0V8a5.6 5.6 0 1 0-2.2 4.4" fill="none" stroke="#fff" stroke-width="1.3"/></symbol>
    <symbol id="icon-mail" viewBox="0 0 16 16"><circle cx="8" cy="8" r="8" fill="#1d8596"/><rect x="4" y="5" width="8" height="6" fill="none" stroke="#fff" stroke-width="1.2"/><path d="M4 5l4 3.4L12 5" fill="none" stroke="#fff" stroke-width="1.2"/></symbol>
    <symbol id="icon-phone" viewBox="0 0 16 16"><circle cx="8" cy="8" r="8" fill="#1d8596"/><path d="M5.3 4.2l1.5-.3.8 2-1 .8a5.5 5.5 0 0 0 2.7 2.7l.8-1 2 .8-.3 1.5c-.2.5-.8.8-1.4.7A7 7 0 0 1 4.6 5.6c-.1-.6.2-1.2.7-1.4z" fill="#fff"/></symbol>
  </defs>
</svg>

<article class="flyer">
  <header class="flyer__header">
    <div class="flyer__rule flyer__rule--left"></div>
    <div class="flyer__rule flyer__rule--right"></div>
  </header>
  <div class="flyer__photo" role="img" aria-label="Photograph of a modern multi-storey waterfront apartment building with balconies under a blue sky"></div>
  <div class="flyer__brand">Harbourleaf Estates Agency</div>

  <section class="offer">
    <p class="offer__lead">Invite your friends<br>and receive</p>
    <p class="offer__amount">$250</p>
    <p class="offer__sub">and they get 2 months</p>
    <p class="offer__perk">Free management! *</p>
  </section>

  <p class="terms">* $250 referral fee paid when the owner you refer signs their property for Management with Harbourleaf Estates Agency. Your referral must be submitted prior to signing on our website using the referral form on this page:<br>http://www.harbourleafestates.com.au/referral-program/</p>

  <footer class="flyer__footer">
    <div class="flyer__footer-brand">Harbourleaf Estates Agency</div>
    <ul class="contact-list">
      <li><svg class="contact-icon"><use href="#icon-web"/></svg>www.harbourleafestates.com.au</li>
      <li><svg class="contact-icon"><use href="#icon-mail"/></svg>referrals@harbourleafestates.com.au</li>
      <li><svg class="contact-icon"><use href="#icon-phone"/></svg>0491 570 156</li>
    </ul>
  </footer>
  <div class="flyer__base"></div>
</article>

<aside class="banner">
  <div class="banner__photo" role="img" aria-label="Photograph of a modern waterfront apartment building fading into a navy background"></div>
  <div class="banner__brand">Harbourleaf Estates Agency</div>
  <ul class="banner__contacts">
    <li>www.harbourleafestates.com.au<svg class="contact-icon"><use href="#icon-web"/></svg></li>
    <li>referrals@harbourleafestates.com.au<svg class="contact-icon"><use href="#icon-mail"/></svg></li>
    <li>0491 570 156<svg class="contact-icon"><use href="#icon-phone"/></svg></li>
  </ul>
  <section class="banner__offer">
    <p class="offer__lead">Invite your friends<br>and receive</p>
    <p class="offer__amount">$250</p>
    <p class="offer__sub">and they get 2 months</p>
    <p class="offer__perk">Free management! *</p>
  </section>
</aside>

</body>
</html>
```